BriarFen Anesthesia Partners, PC

I need a business card /logo for my new business. I would like it to have some type of ? EKG or medical symbol built into the name( I am on the North side of Lake Tessaly where mountains and water are visible.
I would like this saying on the front," Let our Passion Be your Solution"
My company provides anesthesia services to outparient endoscopy units, eye centers, pain & podiatry offices.

Target Market(s)

Gastroenterologists, podiatrists, eye doctors, pain doctors

Industry/Entity Type

Medical

Contact Information for Business Card

I would like to incorporate a medical symbol(EKG, stethoscope, etc) into the name or scenery if possible

Colors
3377b5
add136
fbee3d

Requirements
Must have
• Business name( BriarFen Anesthesia Partners,PCI).....
• "Let Our Passion Be your Solution",
• my email: briarfenanesthesiapartners.example,
• 555-214-9087
Nice to have
• Incorporate water &/or mountains

```html
<!DOCTYPE html>
<html lang="en">
<head>
<meta charset="utf-8">
<title>BriarFen Anesthesia Partners, PC — Business Card</title>
<link href="https://fonts.googleapis.com/css2?family=Cabin+Condensed:wght@400&family=Raleway:wght@300&family=Roboto:wght@400&display=swap" rel="stylesheet">
<style>
  :root {
    --page-bg: #e9e9ea;
    --sky-top: #1e2d4a;
    --sky-mid: #3b4f78;
    --horizon-glow: #c9773e;
    --horizon-dusk: #5a3f55;
    --water-top: #414e72;
    --water-deep: #252d47;
    --brand-blue: #3377b5;
    --brand-pale: #9cc2e8;
    --brand-yellow: #fbee3d;
    --text-light: #f2f3f7;
    --text-soft: #d6dbe8;
  }
  * { box-sizing: border-box; margin: 0; padding: 0; }
  html, body {
    width: 1200px; height: 1000px; overflow: hidden;
    background: var(--page-bg);
  }
  .sheet {
    width: 1200px; height: 1000px;
    display: flex; flex-direction: column; align-items: center; justify-content: center;
    gap: 48px;
  }
  .card {
    position: relative;
    width: 770px; height: 440px;
    border-radius: 4px;
    overflow: hidden;
    box-shadow: 0 6px 18px rgba(0,0,0,0.18);
  }
  .card__scene {
    position: absolute; inset: 0;
    background:
      linear-gradient(180deg,
        var(--sky-top) 0%,
        var(--sky-mid) 26%,
        var(--horizon-dusk) 38%,
        var(--horizon-glow) 44%,
        var(--water-top) 48%,
        var(--water-deep) 100%);
  }
  .card--back .card__scene {
    background:
      linear-gradient(180deg,
        #1b2438 0%,
        #2d3a5a 24%,
        #4a3a52 34%,
        #8a5a4a 38%,
        #3e4a6c 42%,
        var(--water-deep) 100%);
  }
  .brand {
    position: absolute;
    font-family: "Cabin Condensed", "Arial Narrow", sans-serif;
    font-weight: 400;
    letter-spacing: 1px;
    line-height: 1;
    white-space: nowrap;
  }
  .brand--front {
    left: 92px; top: 188px;
    font-size: 46px;
    color: var(--text-light);
  }
  .brand--back {
    left: 60px; top: 120px;
    font-size: 40px;
    color: var(--brand-pale);
  }
  .tagline {
    position: absolute;
    font-family: "Raleway", "Helvetica Neue", sans-serif;
    font-weight: 300;
    letter-spacing: 2px;
    color: var(--text-soft);
    white-space: nowrap;
    line-height: 1;
  }
  .tagline--front { left: 346px; top: 264px; font-size: 19px; }
  .tagline--back { left: 140px; top: 176px; font-size: 17px; }
  .contact {
    position: absolute;
    right: 34px; bottom: 46px;
    display: flex; flex-direction: column; align-items: flex-end; gap: 18px;
    font-family: "Roboto", "Helvetica", sans-serif;
    color: var(--text-light);
  }
  .contact__row { display: flex; align-items: center; gap: 12px; }
  .contact__phone { font-size: 24px; letter-spacing: 1px; }
  .contact__web { font-size: 17px; letter-spacing: 0.5px; }
  .contact__icon { width: 36px; height: 36px; flex: none; }
</style>
</head>
<body>
<main class="sheet">

  <section class="card card--front" aria-label="Card front">
    <div class="card__scene" role="img" aria-label="Photograph of a wooden dock reaching into a lake at sunset, with birds flying over the water"></div>
    <div class="brand brand--front">BriarFen Anesthesia Partners PCI</div>
    <div class="tagline tagline--front">Let Our Passion Be your Solution</div>
  </section>

  <section class="card card--back" aria-label="Card back">
    <div class="card__scene" role="img" aria-label="Photograph of a wooden dock over rippling lake water at dusk, with birds in flight"></div>
    <div class="brand brand--back">BriarFen Anesthesia Partners PCI</div>
    <div class="tagline tagline--back">Let Our Passion Be your Solution</div>

    <div class="contact">
      <div class="contact__row">
        <span class="contact__phone">555-214-9087</span>
        <svg class="contact__icon" viewBox="0 0 36 36" aria-hidden="true">
          <circle cx="18" cy="18" r="15" fill="none" stroke="var(--brand-yellow)" stroke-width="3"/>
          <path d="M13 11c1-1 2-1 3 0l1.5 2.5c.4.8.2 1.5-.5 2l-1 .8c.8 1.8 2 3 3.8 3.8l.8-1c.5-.7 1.2-.9 2-.5L25 20c1 1 1 2 0 3l-1 1c-4 1-12-7-11-11z" fill="var(--text-light)"/>
        </svg>
      </div>
      <div class="contact__row">
        <span class="contact__web">briarfenanesthesiapartners.example</span>
        <svg class="contact__icon" viewBox="0 0 36 36" aria-hidden="true">
          <circle cx="18" cy="18" r="15" fill="none" stroke="var(--brand-yellow)" stroke-width="3"/>
          <rect x="10.5" y="12.5" width="15" height="11" fill="var(--text-light)"/>
          <polyline points="10.5,12.5 18,19 25.5,12.5" fill="none" stroke="var(--water-deep)" stroke-width="1.4"/>
        </svg>
      </div>
    </div>
  </section>

</main>
</body>
</html>
```